Corporate Identity Pack - LetterHead, Business Card, Envelope

We are looking for a clean, professional, and visually connected corporate identity set for our company "VELTA HOME" (Cleaning, Gardening, and Pest Control services).

The pack must include:

Business Card (front and back)
Envelope with recipient window on the right side (22x11)
A4 Letterhead

We provide:
Our final logo (PNG)
Three design references (Inspiration1, Inspiration2, Inspiration3) to spark ideas — but you are absolutely free to propose your own creative solutions based on these concepts.

What we want:
A clean, modern, and trustworthy style
A subtle but creative watermark or graphic detail on the letterhead (not too invasive)

The same visual "family feeling" across business card, envelope, and letterhead: designs must be different but clearly connected

Strong readability for all text and contact details

Use our brand colors (Navy Blue, Green, Orange/Red) in a smart, non-overloaded way

No strict limitations: we are open to creative proposals as long as they are coherent, elegant, and suitable for professional use

Technical specifications:
100% full A4 page layout (no accidental borders)

Deliver ready-to-print PDFs and vector files (AI, EPS)

Respect 5 mm safety margins

Standard sizes for A4, business card, envelope C6 with window at the right

Tone:
Modern – Clean – Elegant – Creative – Trustworthy

Target Market(s)

Professional businesses, property managers, condominium administrators, companies, clinics, and offices requiring cleaning, gardening, and pest control services. The design must convey trust, reliability, professionalism, and attention to detail.

Industry/Entity Type

Cleaning Services, Gardening Services, Pest Control Services

Colors
0054AA
0677BA
7BADD7
CADEEF
E8F1F8
59FF00
82FF00
B8FF75
E3FFCB
F4FFEA
EB3D1F
EC4F4E
F09395
F8D3D4
FCEDEE

Requirements
Must have
• Cohesive design across business card, letterhead, and envelope Clean, modern, professional look Use of brand colors: Navy Blue (main), Green, Orange/Red accents Letterhead must include a subtle watermark without interfering with text Envelope must be with a transparent window for recipient address visibility High readability of all text and contact details Proper alignment, no unnecessary margins (full A4 layout)
Nice to have
• Creative but discreet use of the checkmark from the logo as part of the background or watermark Slight variation or accent of color tones while respecting brand identity A clean visual accent that gives a sense of movement or dynamic professionalism (without being distracting) Icons for email, phone, and website on the business card (if stylistically appropriate)
Should not have
• Overuse of colors or rainbow effects Heavy backgrounds or complex textures that interfere with readability Fonts that are too playful, comic-style, or non-professional Overcrowded layouts — the design must feel clean and spacious Watermarks that are too strong or central (they must be subtle and marginal)

```html
<!DOCTYPE html>
<html lang="en">
<head>
<meta charset="utf-8">
<title>Velta Home – Corporate Identity</title>
<link href="https://fonts.googleapis.com/css2?family=Source+Sans+3:wght@300;400;600;700&display=swap" rel="stylesheet">
<style>
:root{
  --navy:#252a57;
  --orange:#eb5a1f;
  --green:#6fb53b;
  --ink:#2b2f52;
  --paper:#ffffff;
  --mist:#ececee;
}
*{margin:0;padding:0;box-sizing:border-box}
html,body{width:1200px;height:1200px;overflow:hidden}
body{position:relative;background:var(--paper);font-family:"Source Sans 3",sans-serif;color:var(--ink)}
.backdrop{position:absolute;inset:0}
.abs{position:absolute}
.brand{font-family:"Source Sans 3",sans-serif;font-weight:700;color:var(--navy);white-space:nowrap;display:flex;align-items:center;letter-spacing:.02em}
.brand .dot{display:inline-block;background:var(--navy);margin-right:.35em}
.tri{height:3px;background:linear-gradient(90deg,var(--navy) 0 33.33%,var(--orange) 33.33% 66.66%,var(--green) 66.66%)}
.sheet{background:var(--paper);box-shadow:0 3px 10px rgba(0,0,0,.18)}

/* letterhead */
.letterhead{left:94px;top:138px;width:583px;height:825px}
.letterhead .band{position:absolute;left:0;right:0;top:151px;height:397px;background:linear-gradient(180deg,#fff 0%,var(--mist) 18%,#efeff1 60%,#e2e2e5 100%)}
.letterhead .head-brand{left:66px;top:88px;font-size:19px}
.letterhead .head-brand .dot{width:17px;height:17px}
.letterhead .head-brand-alt{right:65px;top:83px;font-size:22px}
.letterhead .head-brand-alt .dot{width:38px;height:38px}
.letterhead .rule-top{left:66px;width:453px;top:148px}
.letterhead .meta{left:66px;top:184px;font-size:11px;line-height:14.8px;font-weight:300}
.letterhead .body{left:66px;top:285px;width:453px;font-size:11px;line-height:14.8px;font-weight:300;text-align:justify}
.letterhead .body p{margin-bottom:14.8px}
.letterhead .sign{left:66px;top:614px;font-size:11px;line-height:14.8px;font-weight:300}
.letterhead .sign .name{font-weight:400}
.letterhead .sign .role{color:#6a6d85}
.letterhead .signature{left:68px;top:643px;width:60px;height:44px;background:linear-gradient(135deg,#f3f3f6,#e6e6ec);border-radius:4px}
.letterhead .rule-bottom{left:66px;width:453px;top:716px}
.footer{display:flex;font-size:8.4px;line-height:11px;font-weight:300}
.footer b{font-weight:600}
.footer .col{display:flex;gap:5px}
.footer svg{flex:none;fill:var(--navy)}
.footer .rows div{display:flex;align-items:center;gap:5px;height:16px}
.pill{display:inline-block;border:1px solid var(--navy);border-radius:6px;padding:0 4px;font-weight:600;font-size:7.5px;line-height:9px;margin-right:5px}
.letterhead .footer{left:66px;top:730px;width:453px;justify-content:space-between}

/* business cards */
.card{left:727px;width:378px;height:213px;border-radius:9px;box-shadow:0 3px 10px rgba(0,0,0,.12);overflow:hidden}
.card-front{top:138px}
.card-front .brand{left:69px;top:91px;font-size:32px}
.card-front .brand .dot{width:28px;height:28px}
.card-back{top:367px}
.card-back .brand{left:26px;top:33px;font-size:22px}
.card-back .brand .dot{width:38px;height:38px}
.card-back .person{right:24px;top:64px;text-align:right;font-weight:300}
.card-back .person .name{font-size:10px;font-weight:400}
.card-back .person .role{font-size:7px;margin-top:6px}
.card-back .tri{left:0;right:0;top:126px}
.card-back .footer{left:24px;right:24px;top:142px;font-size:5.3px;line-height:7.6px;justify-content:space-between}
.card-back .footer .rows div{height:11px;gap:4px}
.card-back .pill{font-size:5px;line-height:6px;padding:0 3px;border-radius:4px;margin-right:4px}

/* envelopes */
.env-back{left:746px;top:656px;width:412px;height:288px;background:var(--paper);box-shadow:0 3px 10px rgba(0,0,0,.15)}
.env-back .flap{position:absolute;left:0;top:0;width:412px;height:58px}
.env-back .brand{left:41px;top:85px;font-size:12px}
.env-back .brand .dot{width:20px;height:20px}
.env-back .edge{position:absolute;right:0;bottom:0;width:40px;height:5px;background:var(--green)}
.env-front{left:707px;top:772px;width:412px;height:289px}
.env-front .brand-top{right:47px;top:42px;font-size:12px}
.env-front .brand-top .dot{width:20px;height:20px}
.env-front .window{left:220px;top:102px;width:159px;height:105px;border:1px solid #d7d7dc;border-radius:12px;background:linear-gradient(180deg,#fff 0%,#f0f0f2 55%,#e3e3e6 100%)}
.env-front .address{right:13px;bottom:13px;text-align:right;font-size:7.6px;line-height:10.5px;font-weight:300}
.env-front .brand-bottom{left:46px;top:235px;font-size:19px}
.env-front .brand-bottom .dot{width:18px;height:18px}
.env-front .tri{position:absolute;left:0;right:0;bottom:0;height:5px}

/* showcase */
.hero-brand{left:94px;top:994px;font-size:60px}
.hero-brand .dot{width:46px;height:46px;margin-right:.4em}
</style>
</head>
<body>

<svg class="backdrop" width="1200" height="1200" aria-hidden="true">
  <polygon points="0,0 1200,0 1200,429 0,741" fill="var(--navy)"/>
</svg>

<!-- A4 letterhead -->
<section class="abs sheet letterhead">
  <div class="band"></div>
  <div class="abs brand head-brand"><span class="dot"></span>VELTA HOME</div>
  <div class="abs brand head-brand-alt"><span class="dot"></span>VELTA HOME</div>
  <div class="abs tri rule-top"></div>

  <div class="abs meta">
    Date: May 01, 2025<br>Name Surname<br>Address<br>Mobile Phone<br>Subject: Lorem Ipsum Dolor Sit Amet
  </div>

  <div class="abs body">
    <p>Lorem ipsum dolor sit amet, consectetur adipiscing elit, sed do eiusmod tempor incididunt ut labore et dolore magna aliqua. Nulla at volutpat diam ut venenatis tellus in. Posuere morbi leo urna molestie. Nibh sit amet commodo nulla facilisi nullam vehicula ipsum a. Sit amet aliquam id diam. Id interdum velit laoreet id donec ultrices tincidunt.</p>
    <p>Consequat mauris nunc congue nisi vitae suscipit tellus. Nulla porttitor massa id neque aliquam vestibulum morbi. Dui accumsan sit amet nulla facilisi morbi tempus iaculis urna. In arcu cursus euismod quis viverra. Posuere urna nec tincidunt praesent semper feugiat. Ut tortor pretium viverra suspendisse potenti nullam ac. Risus pretium quam vulputate dignissim suspendisse in est.</p>
    <p>Feugiat pretium nibh ipsum consequat nisl vel pretium lectus. Mus mauris vitae ultricies leo integer malesuada nunc vel. Mattis molestie a iaculis at erat pellentesque adipiscing commodo elit. Est placerat in egestas erat imperdiet. Vivamus arcu felis bibendum ut tristique et egestas quis ipsum. Neque viverra justo nec ultrices. Aliquet lectus proin nibh nisl condimentum id. Velit laoreet id donec ultrices tincidunt arcu non sodales.</p>
    <p>Urna et pharetra pharetra massa massa ultricies mi. Tortor id aliquet lectus proin nibh nisl condimentum id venenatis. Accumsan in nisl nisi scelerisque eu ultrices. Suspendisse faucibus interdum posuere lorem ipsum dolor sit.</p>
    <p>Pharetra magna ac placerat vestibulum.</p>
  </div>

  <div class="abs sign"><div class="name">NAME SURNAME</div><div class="role">Executive Manager</div></div>
  <div class="abs signature" role="img" aria-label="Handwritten signature"></div>

  <div class="abs tri rule-bottom"></div>
  <div class="abs footer">
    <div class="col">
      <svg width="7" height="10" viewBox="0 0 10 14"><path d="M5 0a5 5 0 0 0-5 5c0 4 5 9 5 9s5-5 5-9a5 5 0 0 0-5-5zm0 7a2 2 0 1 1 0-4 2 2 0 0 1 0 4z"/></svg>
      <div><b>Velta Home SRL</b><br><b>Societa Unipersonale - Einzenlunternehmen</b><br>Via dei Tigli 8 - Lindenweg 8<br>I-39100 Borgo Nuovo (Bz)<br>REA - VWV Nr. Bz 100200 | P.I. - MwSt. 01234567890</div>
    </div>
    <div class="rows">
      <div><svg width="10" height="7" viewBox="0 0 14 10"><path d="M0 0h14v10H0zM1 1l6 5 6-5"/></svg>office@veltahome.example</div>
      <div><svg width="8" height="8" viewBox="0 0 10 10"><path d="M2 0l2 3-1 1c1 2 2 3 3 3l1-1 3 2-1 2C4 10 0 6 0 2z"/></svg>(+39) 300 555 01 23</div>
      <div><svg width="9" height="9" viewBox="0 0 10 10"><circle cx="5" cy="5" r="4.5" fill="none" stroke="var(--navy)"/><path d="M0.5 5h9M5 .5c-3 3-3 6 0 9M5 .5c3 3 3 6 0 9" fill="none" stroke="var(--navy)" stroke-width=".8"/></svg>www.veltahome.example</div>
    </div>
    <div class="rows">
      <div><span class="pill">PEC</span>info.veltahome@pec.example</div>
      <div><span class="pill">SDI</span>K7TQZ20</div>
    </div>
  </div>
</section>

<!-- business card front -->
<section class="abs sheet card card-front">
  <div class="abs brand"><span class="dot"></span>VELTA HOME</div>
</section>

<!-- business card back -->
<section class="abs sheet card card-back">
  <div class="abs brand"><span class="dot"></span>VELTA HOME</div>
  <div class="abs person"><div class="name">NAME SURNAME</div><div class="role">Executive Manager</div></div>
  <div class="abs tri"></div>
  <div class="abs footer">
    <div class="col">
      <svg width="5" height="7" viewBox="0 0 10 14"><path d="M5 0a5 5 0 0 0-5 5c0 4 5 9 5 9s5-5 5-9a5 5 0 0 0-5-5zm0 7a2 2 0 1 1 0-4 2 2 0 0 1 0 4z"/></svg>
      <div><b>Velta Home SRL</b><br><b>Societa Unipersonale - Einzenlunternehmen</b><br>Via dei Tigli 8 - Lindenweg 8<br>I-39100 Borgo Nuovo (Bz)<br>REA - VWV Nr. Bz 100200 | P.I. - MwSt. 01234567890</div>
    </div>
    <div class="rows">
      <div><svg width="7" height="5" viewBox="0 0 14 10"><path d="M0 0h14v10H0zM1 1l6 5 6-5"/></svg>office@veltahome.example</div>
      <div><svg width="5" height="5" viewBox="0 0 10 10"><path d="M2 0l2 3-1 1c1 2 2 3 3 3l1-1 3 2-1 2C4 10 0 6 0 2z"/></svg>(+39) 300 555 01 23</div>
      <div><svg width="6" height="6" viewBox="0 0 10 10"><circle cx="5" cy="5" r="4.5" fill="none" stroke="var(--navy)"/><path d="M0.5 5h9M5 .5c-3 3-3 6 0 9M5 .5c3 3 3 6 0 9" fill="none" stroke="var(--navy)" stroke-width=".8"/></svg>www.veltahome.example</div>
    </div>
    <div class="rows">
      <div><span class="pill">PEC</span>info.veltahome@pec.example</div>
      <div><span class="pill">SDI</span>K7TQZ20</div>
    </div>
  </div>
</section>

<!-- envelope back -->
<section class="abs env-back">
  <svg class="flap" viewBox="0 0 412 58" aria-hidden="true"><path d="M0 0H412L402 35Q396 58 372 58H40Q16 58 10 35Z" fill="var(--navy)"/></svg>
  <div class="abs brand"><span class="dot"></span>VELTA HOME</div>
  <div class="edge"></div>
</section>

<!-- envelope front -->
<section class="abs sheet env-front">
  <div class="abs brand brand-top"><span class="dot"></span>VELTA HOME</div>
  <div class="abs window">
    <div class="abs address">Date: May 01, 2025<br>Name Surname<br>Address<br>Mobile Phone<br>Subject: Lorem Ipsum Dolor Sit Amet</div>
  </div>
  <div class="abs brand brand-bottom"><span class="dot"></span>VELTA HOME</div>
  <div class="tri"></div>
</section>

<!-- primary brand lockup -->
<div class="abs brand hero-brand"><span class="dot"></span>VELTA HOME</div>

</body>
</html>
```